Association le rameau de Tiburel needs a web design design

hello I would like to redo the website of my charity for it to be clearer and more profesional,our association is involved in a orphanage in haiti in port- au-prince here is the first site I did, but it is not very pretty or very credible.

http://rametiburel.sitevela.org/ramet

Industry/Entity Type

Charity

```html
<!DOCTYPE html>
<html lang="fr">
<head>
<meta charset="utf-8">
<title>Rametiburel – Association le rameau de Tiburel</title>
<link href="https://fonts.googleapis.com/css2?family=Roboto+Condensed:wght@400;700&family=Open+Sans:wght@400;600&display=swap" rel="stylesheet">
<style>
:root{
  --pink:#c4428c;
  --pink-light:#d65aa2;
  --pink-dark:#b03479;
  --green:#6ea51c;
  --green-light:#84bd2a;
  --ink:#2b2b2b;
  --body:#555;
  --orange:#e98a1e;
  --page:#f3f3f3;
  --outer:#ececec;
  --footer:#2a2a2a;
  --white:#fff;
}
*{box-sizing:border-box;margin:0;padding:0}
html,body{width:990px;height:1200px;overflow:hidden}
body{background:var(--outer);font-family:"Open Sans",sans-serif;color:var(--body);position:relative}
.sheet{position:absolute;left:82px;top:0;width:828px;height:1200px;background:var(--page);border-left:1px solid #e3e3e3;border-right:1px solid #e3e3e3}
.wrap{position:absolute;left:96px;width:800px}
.head{font-family:"Roboto Condensed",sans-serif;text-transform:uppercase;font-weight:700}

/* header */
.masthead{top:0;height:83px;display:flex;background:linear-gradient(var(--pink-light),var(--pink-dark))}
.brand{width:162px;display:flex;align-items:center;gap:8px;padding-left:18px;color:var(--white);font-family:"Open Sans",sans-serif;font-size:24px;font-weight:400}
.brand i{width:14px;height:14px;background:var(--white);display:block}
.nav{display:flex}
.nav a{width:160px;padding:24px 0 0 21px;color:var(--white);text-decoration:none;border-left:1px solid rgba(255,255,255,.18)}
.nav a.on{background:linear-gradient(var(--green-light),var(--green));border:none}
.nav b{display:block;font-family:"Roboto Condensed",sans-serif;font-size:16px;text-transform:uppercase}
.nav span{font-size:9.5px;display:block;margin-top:4px}

/* hero */
.hero{top:83px;height:363px;background:linear-gradient(120deg,#6e4a36,#a77b5c 40%,#8a6a55 65%,#56606f);}
.hero .cap{position:absolute;left:0;bottom:0;width:100%;height:54px;background:rgba(40,40,40,.8);color:var(--white);font-size:18px;padding:17px 18px}
.arrow{position:absolute;top:194px;width:26px;height:26px;border-radius:50%;border:1px solid rgba(255,255,255,.35)}

/* columns */
.col{position:absolute;top:476px}
.col h2{font-size:18px;color:var(--ink);margin-bottom:14px}
.col h3{font-family:"Open Sans",sans-serif;font-size:9.5px;font-weight:600;text-transform:uppercase;color:var(--ink);line-height:16px;margin-bottom:8px}
.col p{font-size:9.5px;line-height:18.5px}
.col p+p{margin-top:18px}
.date{color:var(--orange);font-size:9.5px;margin-bottom:6px}
.btn{position:absolute;top:691px;width:134px;height:33px;border-radius:3px;background:linear-gradient(var(--green-light),var(--green));color:var(--white);font-family:"Roboto Condensed",sans-serif;font-size:10px;font-weight:700;text-transform:uppercase;display:flex;align-items:center;justify-content:center;box-shadow:0 8px 6px -6px rgba(0,0,0,.3)}
.dots{position:absolute;display:flex;gap:4px}
.dots i{width:10px;height:10px;border-radius:50%;background:#cfcfcf;display:block}
.portrait{width:200px;height:104px;background:linear-gradient(90deg,#1a1a1a,#7a7a7a 55%,#2a2a2a);margin-bottom:14px}

/* banner */
.banner{top:768px;height:86px;background:var(--white);border:1px solid #e2e2e2;box-shadow:0 2px 2px rgba(0,0,0,.06)}
.banner h4{position:absolute;left:19px;top:24px;color:var(--green);font-size:13.5px}
.banner p{position:absolute;left:19px;top:48px;font-size:11px;color:var(--body)}
.donate{position:absolute;right:18px;top:30px;width:127px;height:33px;border-radius:3px;background:linear-gradient(var(--pink-light),var(--pink-dark));color:var(--white);font-family:"Roboto Condensed",sans-serif;font-size:12px;display:flex;align-items:center;justify-content:center;box-shadow:0 8px 6px -6px rgba(0,0,0,.3)}

/* gallery */
.gallery-title{top:880px;font-size:18px;color:var(--ink);left:102px}
.thumbs{top:917px;display:flex;gap:13px}
.thumb{width:123px;height:103px;background:var(--white);border:1px solid #e3e3e3;padding:8px;box-shadow:0 3px 0 #fff,0 4px 0 #ddd}
.thumb div{width:100%;height:100%}

/* footer */
.footer{top:1060px;height:124px;background:var(--footer);color:#cfcfcf;font-size:8px;text-transform:uppercase;text-align:center}
.footer .row{margin-top:27px;word-spacing:2px}
.footer .row+.row{margin-top:13px}
.footer em{font-style:normal;margin:0 9px}
.social{display:flex;justify-content:center;gap:7px;margin-top:15px}
.social i{width:23px;height:23px;border-radius:50%;background:#6a6a6a;display:block}
</style>
</head>
<body>
<div class="sheet"></div>

<header class="wrap masthead">
  <div class="brand"><i></i>rametiburel</div>
  <nav class="nav">
    <a class="on"><b>The Association</b><span>Welcome to our Association</span></a>
    <a><b>The Orphanage</b><span>View info Orphanage</span></a>
    <a><b>News</b><span>View our Latest news</span></a>
    <a><b>Donations</b><span>Click here for donate here</span></a>
  </nav>
</header>

<section class="wrap hero" role="img" aria-label="Photo de trois enfants souriants devant un mur de briques">
  <span class="arrow" style="left:14px"></span>
  <span class="arrow" style="right:14px"></span>
  <div class="cap head">Bienvenue sur le site de l'Association le rameau de Tiburel</div>
</section>

<section class="col" style="left:102px;width:308px">
  <h2 class="head" style="margin-left:2px">About Rametiburel</h2>
  <h3>Bienvenue sur le site de l'association le rameau de l'orphelinat d'Haïti</h3>
  <p>L'association RAMET structure de juin de is etablie non lucrative à Genève, AFIN de devant soutenir l 'Orphelinat le Rameau à Haïti. Créé au lendemain du séisme du 12 janvier 2010.</p>
  <p>L'orphelinat et l'association souhaitent Apporter Leur aide à juin partie des Quelques 100 000 enfants orphelins Que Compte Haïti Suite a this catastrophe.</p>
</section>
<a class="btn" style="left:102px">View more information</a>

<section class="col" style="left:440px;width:202px">
  <h2 class="head" style="margin-left:1px">The Association</h2>
  <div class="portrait" role="img" aria-label="Portrait en noir et blanc d'une jeune fille"></div>
  <p>L'association RAMET structure de juin de is etablie non lucrative à Genève, AFIN de devant soutenir l 'Orphelinat le Rameau...</p>
</section>
<a class="btn" style="left:441px">View more information</a>

<section class="col" style="left:675px;width:220px">
  <h2 class="head" style="margin-left:1px">Latest News</h2>
  <h3>Lorem Ipsum is simply dummy text of the printing</h3>
  <div class="date">Posted on 27 December 2014</div>
  <p>Lorem Ipsum is simply dummy text of the printing and typesetting industry. Lorem Ipsum has been the industry's standard dummy text ever since the 1500s, when an unknown printer took a galley of type and scrambled it to make a type specimen book. It has survived not only...</p>
</section>
<a class="btn" style="left:675px">View more information</a>
<div class="dots" style="left:866px;top:481px"><i></i><i></i></div>

<section class="wrap banner">
  <h4 class="head">Bienvenue sur le site de l'Association le rameau de Tiburel</h4>
  <p>L'association RAMET structure de juin de is etablie non lucrative à Genève, AFIN de devant soutenir l 'Orphelinat le Rameau...</p>
  <a class="donate head">Donate here</a>
</section>

<h2 class="wrap gallery-title head">Photo Gallery</h2>
<div class="dots" style="left:866px;top:891px"><i></i><i></i></div>
<section class="wrap thumbs">
  <div class="thumb"><div role="img" aria-label="Photo de trois personnes assises" style="background:linear-gradient(#4a3a2e,#7d6a55)"></div></div>
  <div class="thumb"><div role="img" aria-label="Photo d'une femme avec des ballons rouges" style="background:linear-gradient(#b52a2a,#3a2a28)"></div></div>
  <div class="thumb"><div role="img" aria-label="Photo d'un groupe lors d'une réception" style="background:linear-gradient(#6b6258,#3b4a70)"></div></div>
  <div class="thumb"><div role="img" aria-label="Photo d'une salle avec des tables" style="background:linear-gradient(#4d5a70,#d9cfb8)"></div></div>
  <div class="thumb"><div role="img" aria-label="Photo d'une soirée dans une salle en pierre" style="background:linear-gradient(#8a8278,#2b2523)"></div></div>
  <div class="thumb"><div role="img" aria-label="Photo d'invités dans une cave voûtée" style="background:linear-gradient(#7a6a58,#2e2824)"></div></div>
</section>

<footer class="wrap footer">
  <div class="row">Accueil<em>/</em>L'association<em>/</em>L'orphelinat<em>/</em>Actualités<em>/</em>Dons<em>/</em>Contact</div>
  <div class="row">© 2015. Rametiburel. All rights reserved. Sitemap<em>/</em>Privacy Policy<em>/</em>Terms &amp; Conditions<em>/</em>Disclaimer</div>
  <div class="social"><i></i><i></i><i></i><i></i><i></i></div>
</footer>
</body>
</html>
```